Consulting Company Business Card

I am looking for a minimalist, classy, professional design on my business card. I would like it to be double-sided. I want to use the font and color scheme of my logo which are attached. Please be creative in the designs that you send me. I want to play off the design of my logo with the inner C that is Green and Blue broken up with the white.
Target Market(s)
Small Businesses
Industry/Entity Type
Consulting
Contact Information for Business Card
Dale M. Whitcombe, CPA CGMA, 555-014-2873, dwhitcombe@vorantaadvisory.example, www.vorantaadvisory.example

```html
<!DOCTYPE html>
<html lang="en">
<head>
<meta charset="utf-8">
<title>Voranta Advisory – Business Card</title>
<link rel="stylesheet" href="https://fonts.googleapis.com/css2?family=Arimo:wght@400;700&family=Montserrat:wght@500&display=swap">
<style>
  :root {
    --backdrop: #d4d4d4;
    --navy: #213559;
    --teal: #2b8a7f;
    --ink: #2a2f3a;
    --paper: #ffffff;
    --rule: rgba(255, 255, 255, 0.35);
  }
  * { margin: 0; padding: 0; box-sizing: border-box; }
  html, body {
    width: 1200px; height: 852px; overflow: hidden;
    background: var(--backdrop);
    font-family: "Arimo", Arial, sans-serif;
  }
  .canvas { position: relative; width: 1200px; height: 852px; }
  .card {
    position: absolute;
    width: 540px; height: 309px;
    border-radius: 22px;
    box-shadow: 0 6px 18px rgba(0, 0, 0, 0.18);
    overflow: hidden;
  }
  /* Back */
  .card-back { left: 70px; top: 110px; background: var(--navy); }
  .card-back .web {
    position: absolute; right: 30px; top: 196px;
    font-family: "Montserrat", Arial, sans-serif; font-weight: 500;
    font-size: 11px; letter-spacing: 4.4px; color: var(--paper);
    white-space: nowrap;
  }
  .card-back .rule {
    position: absolute; left: 34px; right: 26px; top: 218px;
    height: 1px; background: var(--rule);
  }
  .card-back .mark {
    position: absolute; left: 34px; top: 236px;
    display: flex; align-items: center; gap: 10px;
  }
  .card-back .mark .dot {
    width: 38px; height: 38px; border-radius: 50%; background: var(--teal);
  }
  .card-back .mark .name {
    font-weight: 700; font-size: 15px; letter-spacing: 1px; color: var(--paper);
    white-space: nowrap;
  }
  /* Front */
  .card-front { left: 590px; top: 430px; background: var(--paper); }
  .brand {
    position: absolute; right: 34px; top: 44px;
    display: flex; align-items: center; gap: 12px;
  }
  .brand .dot { width: 44px; height: 44px; border-radius: 50%; background: var(--teal); flex: none; }
  .brand .name {
    font-weight: 700; font-size: 24px; line-height: 1.05;
    color: var(--navy); letter-spacing: 1px; text-transform: uppercase;
  }
  .contact { position: absolute; left: 34px; bottom: 34px; }
  .contact .person {
    font-weight: 700; font-size: 19px; color: var(--navy);
    letter-spacing: 1px; text-transform: uppercase;
  }
  .contact .title {
    font-size: 15px; color: var(--teal); margin: 2px 0 10px; letter-spacing: .5px;
  }
  .contact ul { list-style: none; padding-left: 18px; }
  .contact li {
    display: flex; align-items: center; gap: 9px;
    font-size: 14px; color: var(--ink); line-height: 21px; white-space: nowrap;
  }
  .contact svg { width: 13px; height: 13px; fill: var(--teal); flex: none; }
</style>
</head>
<body>
<main class="canvas">
  <section class="card card-back" aria-label="Card back">
    <div class="web">WWW.VORANTAADVISORY.EXAMPLE</div>
    <div class="rule"></div>
    <div class="mark"><span class="dot"></span><span class="name">VORANTA ADVISORY</span></div>
  </section>

  <section class="card card-front" aria-label="Card front">
    <div class="brand"><span class="dot"></span><span class="name">Voranta<br>Advisory</span></div>
    <div class="contact">
      <p class="person">Dale M. Whitcombe</p>
      <p class="title">CPA CGMA</p>
      <ul>
        <li><svg viewBox="0 0 16 16" aria-hidden="true"><path d="M3.5 1 6 3.8 4.6 5.6c.9 2 2.8 4 5 5l1.6-1.4L14 11.7l-1.4 2.6C7 14 2 9 1.8 3z"/></svg>555-014-2873</li>
        <li><svg viewBox="0 0 16 16" aria-hidden="true"><path d="M1 3h14v10H1zM2 4.3v.5l6 4 6-4v-.5z"/></svg>dwhitcombe@vorantaadvisory.example</li>
        <li><svg viewBox="0 0 16 16" aria-hidden="true"><path d="M8 1a7 7 0 1 0 0 14A7 7 0 0 0 8 1zm0 1.5c.8.8 1.5 2.4 1.7 4.5H6.3C6.5 4.9 7.2 3.3 8 2.5zM2.6 7h2.2c.1-1.7.5-3.1 1.1-4.1A5.5 5.5 0 0 0 2.6 7zm0 2a5.5 5.5 0 0 0 3.3 4.1C5.3 12.1 4.9 10.7 4.8 9zm3.7 0h3.4c-.2 2.1-.9 3.7-1.7 4.5C7.2 12.7 6.5 11.1 6.3 9zm4.9 0h2.2a5.5 5.5 0 0 1-3.3 4.1c.6-1 1-2.4 1.1-4.1zm0-2c-.1-1.7-.5-3.1-1.1-4.1A5.5 5.5 0 0 1 13.4 7z"/></svg>www.vorantaadvisory.example</li>
      </ul>
    </div>
  </section>
</main>
</body>
</html>
```